Design a calming beauty medical salon & spa website based in Hong Kong

We need help building an informational website for a beauty salon in Hong Kong. The local salon provides facials, massages, body and other slimming treatments in a relaxing environment. We offer some non-invasive medical treatments, such as botox. Having built the business on word of mouth, it is now time for us to launch a website to help market the business better. Website requirements:

-Must be responsive
-Use vibrant but clean colours. not too many, 1-2 colours
-Must be bilingual (switch between Chinese traditional and English)
-Our current website is host on a server, not using any particular platforms like wordpress

Pages:
1/ Homepage
2/ About us (incorporate gallery of salon photos and history of company)
3/ Promotions and latest deals (and leads them to sign up for more info, maybe pop-up small window when you click on a promotion)
4/ Treatment menus
4.1/Body treatments
4.2/ Face treatments
4.3/ Slimming treatments
5/ Showcasing products sold (no e-commerce functionality, just showing off products)
6/ Contact us (tel, address, map, opening hrs)

Footer - must haves include contact us info, privacy policy, terms & conditions, copyright blurb, join our company/employment page (with a form)

For information (comparable websites we like):
http://vostaria.com/
http://quimbel.com.hk/tc/aboutquimbel/background.php#centerenvi
Attaching a very first draft concept for this website
Attaching pictures of the beauty salon
Attaching logo

Target Market(s)

Hong Kong based, Chinese, females, 30-50+ age. 90% female clients.

Industry/Entity Type

Beauty Salon

Number of Pages Required

5+ page

Font styles to use
Sans Serif

Colors
f9d9e8
fbd3d4
fee3d5
fbe7d2
fee18a
fbf289
ffffff

Requirements
Must have
• interactive elements on website, such as scrolling banner photo headers
• incorporate photos of website salon
• connect to facebook page

```html
<!DOCTYPE html>
<html lang="en">
<head>
<meta charset="utf-8">
<title>Luma Spa – Beauty Salon</title>
<link href="https://fonts.googleapis.com/css2?family=Playfair+Display:wght@400;700&family=Lato:wght@400;700&family=Montserrat:wght@400;600;700&display=swap" rel="stylesheet">
<style>
:root{
  --pink:#f4847e;
  --pink-soft:#f7a19c;
  --dark:#2b2b2b;
  --black:#111111;
  --footer:#1b1b1b;
  --band:#e9e9e9;
  --text:#555555;
  --head:#333333;
  --white:#ffffff;
  --line:#d9d9d9;
}
*{box-sizing:border-box;margin:0;padding:0}
html,body{width:1200px;height:3315px;overflow:hidden}
body{font-family:'Lato',sans-serif;color:var(--text);background:var(--white);position:relative}
.abs{position:absolute}
h1,h2,h3,h4{font-weight:400}
.topbar{top:0;left:0;width:1200px;height:31px;background:var(--dark);color:#ddd;font-size:11px}
.topbar .social{left:236px;top:11px;display:flex;gap:9px}
.dot-icon{width:9px;height:9px;border-radius:50%;background:#bbb;display:block}
.topbar .lang{right:236px;top:9px;letter-spacing:.5px;white-space:nowrap}
.header{top:31px;left:0;width:1200px;height:75px;background:var(--white)}
.brand{left:252px;top:30px;font-family:'Montserrat',sans-serif;font-weight:700;font-size:13px;color:var(--pink);letter-spacing:.5px;display:flex;align-items:center;gap:7px;white-space:nowrap}
.brand i{width:8px;height:8px;background:var(--pink);border-radius:50%;display:block}
.info{top:22px;display:flex;gap:10px;font-size:11px;color:#333;white-space:nowrap}
.info svg{width:26px;height:26px;flex:none}
.info b{display:block;font-weight:700;font-size:12px}
.info small{font-size:9.5px;color:#888}
.nav{top:106px;left:0;width:1200px;height:66px;background:var(--black)}
.nav ul{list-style:none;display:flex;gap:36px;position:absolute;left:494px;top:25px;font-family:'Montserrat',sans-serif;font-size:11.5px;font-weight:600;color:#fff;white-space:nowrap}
.nav .book{left:880px;top:20px;width:86px;height:28px;background:#fff;color:var(--pink);font-size:10.5px;text-align:center;line-height:28px;font-family:'Montserrat',sans-serif}
.hero{top:172px;left:0;width:1200px;height:484px;background:radial-gradient(circle at 20% 20%,#e7b07a 0,#b07451 30%,#6b4a3a 60%,#c9c1b8 100%)}
.hero-card{left:263px;top:115px;width:526px;height:210px;background:rgba(40,40,40,.78);padding:26px 24px;color:#fff}
.hero-card .eyebrow{font-size:15px;font-family:'Montserrat',sans-serif}
.hero-card h1{font-family:'Montserrat',sans-serif;font-weight:700;font-size:27px;margin:8px 0 14px;letter-spacing:.5px;white-space:nowrap}
.hero-card h1 span{color:var(--pink)}
.hero-card p{font-size:10.5px;line-height:1.5;color:#ddd;width:470px}
.btn-white{display:inline-block;margin-top:20px;background:#fff;color:var(--pink);font-size:11px;font-weight:700;padding:10px 20px}
.arrow{width:32px;height:32px;border-radius:50%;top:223px}
.hero-dots{left:578px;top:414px;display:flex;gap:7px}
.hero-dots i{width:8px;height:8px;border-radius:50%;border:1.5px solid #fff;display:block}
.hero-dots i.on{background:#fff}
.section-title{font-family:'Playfair Display',serif;font-weight:400;font-size:33px;color:var(--head);text-align:center;width:1200px;left:0;top:685px;letter-spacing:.5px}
.service{left:0;width:1200px}
.service.grey{background:var(--band)}
.service h2{font-family:'Playfair Display',serif;font-weight:400;font-size:29px;color:var(--head);letter-spacing:.5px;white-space:nowrap}
.service p{font-size:13px;line-height:1.72;color:#555}
.btn-pink{background:var(--pink);color:#fff;font-size:11.5px;text-align:center;width:180px;height:35px;line-height:35px;font-family:'Montserrat',sans-serif;white-space:nowrap}
.products-banner{top:1962px;left:0;width:1200px;height:155px;background:linear-gradient(90deg,#d9cfc9,#efe7e3 50%,#d9cfc9)}
.products-banner h2{font-family:'Playfair Display',serif;font-weight:400;font-size:29px;color:var(--head);text-align:center;width:100%;top:60px}
.card{top:2150px;width:226px;height:199px;border:3px solid var(--pink-soft);background:var(--pink-soft)}
.card .img{height:130px}
.card span{display:block;color:#fff;font-family:'Montserrat',sans-serif;font-size:16px;text-align:center;line-height:62px;text-transform:uppercase;white-space:nowrap}
.pdots{left:580px;top:2374px;display:flex;gap:8px}
.pdots i{width:8px;height:8px;border-radius:50%;border:1.5px solid #333;display:block}
.pdots i.on{background:#333}
.map{top:2420px;left:0;width:1200px;height:619px;background:linear-gradient(135deg,#e6e3dc,#d8dfd2 45%,#e9e5de)}
.contact{left:248px;top:2497px;width:713px;height:486px;background:#fff;box-shadow:0 2px 10px rgba(0,0,0,.15)}
.contact .side{left:455px;top:0;width:258px;height:486px;background:#f3f3f3;padding:95px 30px;font-size:10.5px;color:#444;line-height:1.6}
.contact .side h4{font-size:13px;font-family:'Montserrat',sans-serif;font-weight:600;margin-bottom:38px}
.contact .side b{font-size:10.5px;display:block;margin-top:22px}
.contact h3{font-family:'Playfair Display',serif;font-weight:400;font-size:26px;font-variant:small-caps;color:#222;left:20px;width:415px;text-align:center;top:60px;white-space:nowrap}
.contact .sub{left:20px;width:415px;text-align:center;top:96px;font-family:'Playfair Display',serif;font-variant:small-caps;font-size:13px;color:#333;white-space:nowrap}
.contact .sendmsg{left:62px;top:145px;font-family:'Montserrat',sans-serif;font-size:13px;color:#333}
.field{border:1px solid #ccc;border-radius:3px;height:33px;font-size:9.5px;color:#aaa;padding:11px 12px}
.send{left:62px;top:403px;width:104px;height:33px;background:#1e1e1e;border-radius:3px;color:#fff;font-size:10px;text-align:center;line-height:33px;font-weight:700}
.footer{top:3039px;left:0;width:1200px;height:236px;background:var(--footer);color:#bbb}
.footer h2{font-family:'Playfair Display',serif;font-weight:400;font-size:32px;color:#fff;width:100%;text-align:center;top:50px;letter-spacing:1px}
.footer p{left:360px;top:116px;width:520px;font-size:10px;line-height:1.6}
.fcontact{top:157px;font-size:10px;display:flex;gap:8px;align-items:flex-start;white-space:nowrap}
.fsocial{left:540px;top:205px;display:flex;gap:11px}
.bottombar{top:3275px;left:0;width:1200px;height:40px;background:var(--black);color:#bbb;font-size:9.5px}
.bottombar .copy{left:236px;top:15px;white-space:nowrap}
.bottombar .copy span{color:var(--pink)}
.bottombar ul{list-style:none;display:flex;gap:26px;position:absolute;right:236px;top:15px;color:#ddd}
</style>
</head>
<body>

<div class="abs topbar">
  <div class="abs social"><i class="dot-icon"></i><i class="dot-icon"></i><i class="dot-icon"></i><i class="dot-icon"></i><i class="dot-icon"></i></div>
  <div class="abs lang">LANGUAGE: ENGLISH / CHINESE</div>
</div>

<header class="abs header">
  <div class="abs brand"><i></i>LUMA SPA</div>
  <div class="abs info" style="left:420px">
    <svg viewBox="0 0 26 26"><circle cx="13" cy="13" r="12" fill="#fde4e2"/><circle cx="13" cy="13" r="6.5" fill="none" stroke="#f4847e" stroke-width="1.6"/><path d="M13 9.5V13l2.5 1.5" stroke="#f4847e" stroke-width="1.6" fill="none"/></svg>
    <div><b>Working Hours</b><small>Mon - Sat 9.00 to 17.00</small></div>
  </div>
  <div class="abs info" style="left:610px">
    <svg viewBox="0 0 26 26"><circle cx="13" cy="13" r="12" fill="#fde4e2"/><path d="M13 6.5a4.5 4.5 0 0 1 4.5 4.5c0 3.5-4.5 8.5-4.5 8.5S8.5 14.5 8.5 11A4.5 4.5 0 0 1 13 6.5z" fill="#f4847e"/><circle cx="13" cy="11" r="1.7" fill="#fff"/></svg>
    <div><b>Address</b><small>18 Lotus Lane, Wan Chai, HK</small></div>
  </div>
  <div class="abs info" style="left:836px">
    <svg viewBox="0 0 26 26"><circle cx="13" cy="13" r="12" fill="#fde4e2"/><path d="M9 7.5l2.5-.5 1.3 3-1.6 1.2a8 8 0 0 0 3.6 3.6l1.2-1.6 3 1.3-.5 2.5C14 18 8 12 9 7.5z" fill="#f4847e"/></svg>
    <div><b>Call</b><small>852-2718-3340</small></div>
  </div>
</header>

<nav class="abs nav">
  <ul><li>Home</li><li>About</li><li>Services</li><li>Gallery</li><li>Contact us</li></ul>
  <div class="abs book">Book Now</div>
</nav>

<section class="abs hero" role="img" aria-label="Woman relaxing while receiving a face and head massage in a warm-lit spa">
  <div class="abs hero-card">
    <div class="eyebrow">Welcome to <b>Luma Spa</b></div>
    <h1>A PROFESSIONAL <span>SPA</span> SALON</h1>
    <p>Our calm rooms, gentle hands and tailored care bring quiet comfort to every visit. Relax, restore and leave refreshed with treatments made for you.</p>
    <div class="btn-white">Read More</div>
  </div>
  <svg class="abs arrow" style="left:30px" viewBox="0 0 32 32"><circle cx="16" cy="16" r="16" fill="#111"/><path d="M18 11l-5 5 5 5" stroke="#fff" stroke-width="2" fill="none"/></svg>
  <svg class="abs arrow" style="left:1136px" viewBox="0 0 32 32"><circle cx="16" cy="16" r="16" fill="#111"/><path d="M14 11l5 5-5 5" stroke="#fff" stroke-width="2" fill="none"/></svg>
  <div class="abs hero-dots"><i class="on"></i><i></i><i></i></div>
</section>

<h2 class="abs section-title">OUR SERVICES</h2>

<section class="abs service grey" style="top:762px;height:321px">
  <h2 class="abs" style="left:298px;top:42px">BODY TREATMENTS</h2>
  <p class="abs" style="left:241px;top:96px;width:415px">Lorem ipsum dolor sit amet, consectetuer adipiscing elit. modo ligula eget dolor. Aenean massa. Cum sociis natoque penatibus nis dis parturient montes, nascetur ridiculus mus. DoneFsf srwht zkcec, pellentesque eu, pretium quis, sem. Nulla consequat massa qui Donec pede justo, fringilla vel, aliquet nec, vulputate eget, arcu. Im justo.</p>
  <div class="abs btn-pink" style="left:468px;top:235px">CLAIM YOUR OFFER</div>
  <div class="abs" style="left:685px;top:38px;width:281px;height:234px;background:linear-gradient(135deg,#f2e4d8,#d9a27e 50%,#8a5a43)" role="img" aria-label="Back massage with warm stones"></div>
</section>

<section class="abs service" style="top:1083px;height:322px">
  <div class="abs" style="left:236px;top:37px;width:277px;height:232px;background:linear-gradient(135deg,#3a3a3a,#b78f7a 50%,#2aa59a)" role="img" aria-label="Eyebrow shaping treatment"></div>
  <h2 class="abs" style="left:614px;top:40px">FACE TREATMENTS</h2>
  <p class="abs" style="left:551px;top:96px;width:415px">Lorem ipsum dolor sit amet, consectetuer adipiscing elit. modo ligula eget dolor. Aenean massa. Cum sociis natoque penatibus nis dis parturient montes, nascetur ridiculus mus. DoneFsf srwht zkcec, pellentesque eu, pretium quis, sem. Nulla consequat massa qui Donec pede justo, fringilla vel, aliquet nec, vulputate eget, arcu. Im justo.</p>
  <div class="abs btn-pink" style="left:781px;top:233px">CLAIM YOUR OFFER</div>
</section>

<section class="abs service grey" style="top:1405px;height:321px">
  <h2 class="abs" style="left:260px;top:42px">SLIMMING TREATMENTS</h2>
  <p class="abs" style="left:241px;top:96px;width:415px">Lorem ipsum dolor sit amet, consectetuer adipiscing elit. modo ligula eget dolor. Aenean massa. Cum sociis natoque penatibus nis dis parturient montes, nascetur ridiculus mus. DoneFsf srwht zkcec, pellentesque eu, pretium quis, sem. Nulla consequat massa qui Donec pede justo, fringilla vel, aliquet nec, vulputate eget, arcu. Im justo.</p>
  <div class="abs btn-pink" style="left:468px;top:235px">CLAIM YOUR OFFER</div>
  <div class="abs" style="left:685px;top:40px;width:281px;height:232px;background:linear-gradient(135deg,#5a4a3e,#e0b79a 50%,#c89573)" role="img" aria-label="Shoulder and neck massage"></div>
</section>

<section class="abs service" style="top:1726px;height:236px">
  <div class="abs" style="left:267px;top:35px;width:204px;height:164px;background:linear-gradient(135deg,#3a3a3a,#b78f7a 50%,#2aa59a)" role="img" aria-label="Brow treatment in progress"></div>
  <h2 class="abs" style="left:569px;top:30px;font-size:28px">GET 25% DISCOUNT TODAY</h2>
  <p class="abs" style="left:570px;top:82px;width:396px;font-size:12.5px;line-height:1.72;text-transform:uppercase;color:#444">Lorem ipsum dolor sit amet, consectetuer adipisc ing elit. Aenean commodo ligula eget dolor. Aeneans a. Cum sociis natoque penatibus et magnis dis partur</p>
  <div class="abs btn-pink" style="left:781px;top:166px">CLAIM YOUR OFFER</div>
</section>

<section class="abs products-banner" role="img" aria-label="Soft faded image of a relaxing woman at the spa">
  <h2 class="abs">PRODUCTS SOLD</h2>
</section>

<div class="abs card" style="left:236px"><div class="img" style="background:linear-gradient(135deg,#f3efe6,#d7b66b 50%,#f0ece5)" role="img" aria-label="Gold skincare jars"></div><span>Marlow Riviera</span></div>
<div class="abs card" style="left:488px"><div class="img" style="background:linear-gradient(135deg,#cfcfcf,#e8d23e 50%,#a9a9a9)" role="img" aria-label="Row of yellow serum bottles"></div><span>Sereno Products</span></div>
<div class="abs card" style="left:738px"><div class="img" style="background:linear-gradient(135deg,#f2f2f2,#3e7a3a 50%,#c9d8a8)" role="img" aria-label="Green skincare product set"></div><span>Aliva Products</span></div>
<div class="abs pdots"><i></i><i class="on"></i><i></i></div>

<section class="abs map" role="img" aria-label="City street map showing the salon location"></section>

<section class="abs contact">
  <h3 class="abs">Contact Us</h3>
  <div class="abs sub">Get in touch, we're user-friendly!</div>
  <div class="abs sendmsg">Send a message</div>
  <div class="abs field" style="left:62px;top:197px;width:346px;border-color:#888;color:#333">Email</div>
  <div class="abs field" style="left:62px;top:251px;width:162px">Your name</div>
  <div class="abs field" style="left:245px;top:251px;width:163px">Phone number</div>
  <div class="abs field" style="left:62px;top:305px;width:346px;height:70px">How can we help?</div>
  <div class="abs send">SEND</div>
  <div class="abs side">
    <h4>Information</h4>
    <b>Address #1</b>
    22 Orchid Road<br>Causeway Bay<br>Hong Kong
    <b>Connect with us</b>
    <div style="display:flex;gap:9px;margin-top:6px"><i class="dot-icon" style="background:#777"></i><i class="dot-icon" style="background:#777"></i><i class="dot-icon" style="background:#777"></i><i class="dot-icon" style="background:#777"></i></div>
    <b>working Hours</b>
    Monday - friday<br>9:00AM - 6:00PM
  </div>
</section>

<footer class="abs footer">
  <h2 class="abs">SPA BEAUTY SALON</h2>
  <p class="abs">Calm rooms, caring hands and gentle treatments for face and body. Visit us for a quiet hour of rest and leave feeling fresh, light and renewed every time.</p>
  <div class="abs fcontact" style="left:360px">
    <svg width="12" height="12" viewBox="0 0 12 12"><path d="M6 1a3.5 3.5 0 0 1 3.5 3.5C9.5 7 6 11 6 11S2.5 7 2.5 4.5A3.5 3.5 0 0 1 6 1z" fill="#bbb"/></svg>
    <span>9 Jasmine Terrace,<br>Central, HK</span>
  </div>
  <div class="abs fcontact" style="left:540px">
    <svg width="12" height="12" viewBox="0 0 12 12"><path d="M2.5 1.5l2-.4 1 2.4-1.3 1a6 6 0 0 0 2.8 2.8l1-1.3 2.4 1-.4 2C6 10 2 6 2.5 1.5z" fill="#bbb"/></svg>
    <span>852-2588-1120</span>
  </div>
  <div class="abs fcontact" style="left:694px">
    <svg width="12" height="10" viewBox="0 0 12 10"><rect x=".5" y=".5" width="11" height="9" fill="#bbb"/><path d="M.5 .5L6 5l5.5-4.5" stroke="#1b1b1b" fill="none"/></svg>
    <span>hello@lumaspa.hk</span>
  </div>
  <div class="abs fsocial"><i class="dot-icon" style="background:#777"></i><i class="dot-icon" style="background:#777"></i><i class="dot-icon" style="background:#777"></i><i class="dot-icon" style="background:#777"></i><i class="dot-icon" style="background:#777"></i></div>
</footer>

<div class="abs bottombar">
  <div class="abs copy">Copyright © All Rights Reserved by <span>Luma Spa</span></div>
  <ul><li>Home</li><li>About</li><li>Services</li><li>Shop</li><li>Gallery</li><li>Contact</li></ul>
</div>

</body>
</html>
```